Website for new academic journal of deconstruction and psychoanalysis

- This project has been put on hold because of a mistake I made. I requested that the project be for a journal cover and matching website. The problem was that I was trying to get web designers to design a book cover first, and it was not working. I have started a new project for a book or journal cover. Once that project has been completed, I will bring the book cover design over to this project so that it can be used with the website design. This way this design project can focus on the function of the website. -

The function of the website will be similar to the function of these other KVR journals. I give you these other journals just as examples of journal websites and journal covers:

http://www.qmbr.wexdale.ac.uk/
http://heritage.pfwk.edu/
http://www.hym.tarnwick.edu/~velomarte/
http://www.fathomquarterly.org/subscribe/subscribe-to-fathom/

The EO website will have the following buttons/pages:

Home
About the Journal
Issues
News and Events
Blog
Submissions
Contact
Links
Updates

- This project has been put on hold because of a mistake I made.  I requested that the project be for a journal cover and matching website.  The problem was that I was trying to get web designers to design a book cover first, and it was not working.  I have started a new project for a book or journal cover.  Once that project has been completed, I will bring the book cover design over to this project so that it can be used with the website design.  This way this design project can focus on the function of the website. -

Target Market(s)

Professional academics and psychoanalytic clinicians.

Industry/Entity Type

Events

Font styles to use
Sans Serif

Requirements
Nice to have
• A very contemporary feel. Simplicity. Bold colors.
Should not have
• NO photos of Maltby or Velkano, or photos of anyone. No photos of books or academic icons.

```html
<!DOCTYPE html>
<html lang="en">
<head>
<meta charset="utf-8">
<title>The Errant Other – a journal of deconstruction and psychoanalysis</title>
<link href="https://fonts.googleapis.com/css2?family=PT+Sans:wght@400;700&family=PT+Sans+Caption:wght@700&display=swap" rel="stylesheet">
<style>
:root{
  --night:#05070c;
  --teal:#1f9ab3;
  --teal-dark:#1a8399;
  --teal-light:#31b4cc;
  --ink:#333;
  --muted:#555;
  --lime:#c9e23a;
  --red:#c0262d;
  --panel:#f6f6f6;
  --line:#cfcfcf;
  --footer:#2b2b2b;
}
*{margin:0;padding:0;box-sizing:border-box}
html,body{width:752px;height:1200px;overflow:hidden}
body{position:relative;background:#fff;font-family:"PT Sans",sans-serif;color:var(--ink);font-size:8.5px;line-height:1.55}
.abs{position:absolute}
.masthead{left:0;top:0;width:752px;height:308px;background:
  radial-gradient(ellipse 120px 40px at 40px 190px,rgba(60,130,210,.55),transparent),
  radial-gradient(ellipse 140px 45px at 720px 200px,rgba(60,130,210,.55),transparent),
  radial-gradient(ellipse 420px 60px at 376px 190px,rgba(40,80,150,.35),transparent),
  linear-gradient(#04060a 0%,#060a14 45%,#0b1a33 62%,#0a1323 80%,#05070c 100%)}
.brand{left:109px;top:8px;color:var(--teal);font-family:"PT Sans Caption",sans-serif;font-weight:700;font-size:23px;line-height:24px;letter-spacing:-.3px}
.tagline{left:109px;top:88px;color:var(--teal);font-size:11px;line-height:14px;font-style:italic}
.account{right:75px;top:12px;color:#ddd;font-size:8px;text-align:right;line-height:25px}
.nav{left:306px;top:88px;width:370px;border-top:1px solid var(--teal);display:flex;justify-content:space-between;padding-top:5px;font-size:8.6px;color:#ddd}
.nav .on{color:var(--teal-light);position:relative}
.nav .on::before{content:"";position:absolute;left:9px;top:-6px;border:4px solid transparent;border-top-color:var(--teal)}
.slider{left:82px;top:132px;width:591px;height:246px;background:#222;box-shadow:0 6px 8px rgba(0,0,0,.5)}
.hero{left:4px;top:8px;width:420px;height:231px;background:linear-gradient(135deg,#7a6a57 0%,#c9bba7 35%,#e8e0d4 60%,#bfb09a 100%)}
.caption{left:4px;top:212px;width:420px;height:27px;background:rgba(235,230,222,.85);display:flex;justify-content:space-between;align-items:center;padding:0 70px 0 10px}
.caption b{font-family:"PT Sans Caption",sans-serif;font-size:12px;font-variant:small-caps;color:#222}
.caption span{font-size:7.5px;color:#333}
.thumbs{left:424px;top:8px;width:160px}
.thumb{height:58px;display:flex;align-items:center;gap:9px;padding:0 8px;background:linear-gradient(#3a3a3a,#262626);border-bottom:1px solid #111;color:#eee;font-size:8.4px;line-height:11.5px}
.thumb.active{background:var(--teal);color:#fff;font-weight:700;position:relative}
.thumb.active::before{content:"";position:absolute;left:-7px;top:22px;border:7px solid transparent;border-right-color:var(--teal);border-left:0}
.thumb i{flex:0 0 48px;height:44px;border:2px solid #eee;display:block}
.cover{left:98px;top:400px;width:99px;height:155px;background:linear-gradient(160deg,#1a1a1a 0%,#0b0b0b 60%,#3a3a3a 100%)}
.about h2{font-weight:400;font-size:12px;color:#333;margin-bottom:4px}
.about{left:212px;top:413px;width:280px;color:var(--muted)}
.meta{left:99px;top:583px;width:110px;color:#444;line-height:14.5px}
.meta p{margin-bottom:14px}
.body{left:226px;top:583px;width:255px;color:#444;line-height:13.2px}
.issue{left:86px;width:405px;height:146px;background:var(--panel);border:1px solid var(--line)}
.issue i{position:absolute;left:8px;top:7px;width:85px;height:131px;border:1px solid #ccc;display:block}
.issue .txt{position:absolute;left:101px;top:6px;width:295px;font-size:7.7px;color:#444;line-height:11.5px}
.issue h3{font-weight:400;font-size:9px;color:#333;margin-bottom:3px}
.issue h3.gap{margin-top:14px}
.issue a{display:block;margin-top:14px;color:var(--red);text-decoration:none;font-size:7.6px}
.side{left:506px;top:398px;width:168px;height:678px;background:var(--teal);border:2px solid #cfeaf0}
.side h4{font-weight:400;font-size:12px;color:#fff;padding:10px 0 0 8px}
.field{margin:6px 0 0 8px;width:152px;height:19px;background:#fff;font-size:7px;color:#777;padding:4px 8px;font-style:italic;position:relative}
.go{position:absolute;right:-22px;top:0;width:22px;height:19px;background:var(--lime)}
.browse{color:#fff;font-size:8.5px;padding:10px 0 0 19px}
.band{background:var(--teal-light);margin-top:12px;height:78px}
.send{margin:9px 0 0 102px;width:50px;height:15px;background:#1b1b1b;border-radius:3px;color:#fff;font-size:8px;text-align:center;line-height:15px}
.links{list-style:none;margin-top:20px;padding-left:18px;color:#fff;font-size:8px;line-height:18.2px}
.links li::before{content:"›";margin-right:7px}
.cats{background:var(--teal-dark);margin-top:10px;padding:13px 0 0 16px;height:380px}
.cat{display:flex;gap:12px;height:88px;color:#fff;font-size:7.6px;line-height:11.5px}
.cat i{flex:0 0 55px;height:71px;display:block}
.cat em{font-style:normal;color:var(--lime);display:block;margin-top:3px}
.footer{left:0;top:1092px;width:752px;height:108px;background:var(--footer);color:#ddd;font-size:7.6px;line-height:11.4px}
.footer h5{font-weight:400;font-size:11px;color:#fff}
.social{right:94px;top:25px;display:flex;gap:8px}
.social i{width:16px;height:16px;background:#777;display:block}
</style>
</head>
<body>
<div class="abs masthead"></div>
<div class="abs brand">THE<br>ERRANT<br>OTHER</div>
<div class="abs tagline">a journal of deconstruction<br>and psychoanalysis</div>
<div class="abs account">Journals Log In | Journals Account Info<br>Books Cart &nbsp;|&nbsp; Journals Cart</div>
<nav class="abs nav"><span class="on">Home</span><span>About the Journal</span><span>Issues</span><span>News and Events</span><span>Blog</span><span>Submissions</span><span>Contact</span><span>Links</span></nav>

<div class="abs slider">
  <div class="abs hero" role="img" aria-label="Close-up of a pen resting on a spiral notebook"></div>
  <div class="abs caption"><b>A Journal of Deconstruction and Psychoanalysis</b><span>Sep 19, 2013</span></div>
  <div class="abs thumbs">
    <div class="thumb active"><i role="img" aria-label="Spiral notebook" style="background:linear-gradient(135deg,#d8d0c4,#6d6256)"></i>A Journal of Deconstruction</div>
    <div class="thumb"><i role="img" aria-label="Pale ink illustration" style="background:linear-gradient(135deg,#eef0e8,#9cc6c4)"></i>Mauris vel lacus vitae felis vestibulum volutpat.</div>
    <div class="thumb"><i role="img" aria-label="Red leaves against a sunset" style="background:linear-gradient(#f2b070,#8a4a3a 60%,#c23a4a)"></i>Mauris vel lacus vitae felis vestibulum volutpat.</div>
    <div class="thumb"><i role="img" aria-label="Dark brown book cover" style="background:linear-gradient(#6a3320,#3a1a10)"></i>Mauris vel lacus vitae felis vestibulum volutpat.</div>
  </div>
</div>

<div class="abs cover" role="img" aria-label="Journal cover image"></div>

<div class="abs about">
  <h2>About &nbsp;The Journal</h2>
  <p>A new journal coming soon. New journal launching late 2013. Check this web page for updated subscription information. If you would like to be sent an email when subscriptions are available, click here for the online version (recommended) or here for the print version.</p>
  <p style="margin-top:22px">Deconstruction—the analysis and transformation of metaphysics — intersects with psychoanalysis. Both are engaged with thinking beyond consciousness.</p>
</div>

<div class="abs meta">
  <p>Annual<br>ISSN &nbsp;2391-5520</p>
  <p>Table of Contents</p>
  <p>Submission &amp; Book Review Guidelines and Contacts</p>
  <p style="margin:0">Advertising<br>Permissions<br>Customer Service</p>
</div>
<div class="abs body">This new journal is a forum for those working at the borders of these two disciplines. Its name, The Errant Other, refers to the broadest aspect of psychoanalysis—the theory of unconscious processes—and to Velkano’s thinking about undecidability—the irreducible oscillation and chance of non-metaphysical processes. The name, then, speaks of psychoanalysis as deconstruction. It also invites opening to all fields in which undecidability is at stake. Hence the journal seeks contributions from all disciplines informed by deconstruction and psychoanalysis. Its aim is to enrich, to expand, to change: deconstruction, psychoanalysis, and everything that they touch upon.</div>

<div class="abs issue" style="top:766px">
  <i role="img" aria-label="Pale journal cover with an ink drawing" style="background:linear-gradient(160deg,#f3ece0,#d9d4c6)"></i>
  <div class="txt">
    <h3>Contents</h3>
    <p>The Divided Legacy of the Republic of : Emancipation and Trauma – Radko Vesnic</p>
    <p style="margin-top:3px">A Howl and a Black Cat: Allegory, Nonsense, and Ethics in Oren Talbis’s Lantern and Moth – Lena Harrow</p>
    <h3 class="gap">Book Review</h3>
    <p>Carla Denvit, The Nature of Trauma in American Novels - Mirela Sandqvist</p>
    <a>Read More &gt;&gt;</a>
  </div>
</div>
<div class="abs issue" style="top:930px">
  <i role="img" aria-label="Journal cover with a bare winter landscape" style="background:linear-gradient(#e8e3b8,#8c8a78 60%,#3a3a34)"></i>
  <div class="txt">
    <h3>Contents</h3>
    <p>The Divided Legacy of the Republic of : Emancipation and Trauma – Radko Vesnic</p>
    <p style="margin-top:3px">A Howl and a Black Cat: Allegory, Nonsense, and Ethics in Oren Talbis’s Lantern and Moth – Lena Harrow</p>
    <h3 class="gap">Book Review</h3>
    <p>Carla Denvit, The Nature of Trauma in American Novels - Mirela Sandqvist</p>
    <a>Read More &gt;&gt;</a>
  </div>
</div>

<aside class="abs side">
  <h4>Search</h4>
  <div class="field" style="width:131px">Search<span class="go"><svg width="22" height="19" viewBox="0 0 22 19"><circle cx="10" cy="8.5" r="4" fill="none" stroke="#fff" stroke-width="1.8"/><line x1="13" y1="11.5" x2="16" y2="14.5" stroke="#fff" stroke-width="2"/></svg></span></div>
  <div class="browse">Browse Books</div>
  <div class="band">
    <h4>To Receive E-Mail Promos</h4>
    <div class="field">Enter your email</div>
  </div>
  <div class="send" style="margin-top:-26px;position:relative">Send</div>
  <ul class="links"><li>Support The Press</li><li>Read Our Blog</li><li>Special Offers</li><li>Hanukkah Sale</li><li>New November Books</li><li>KVR News</li></ul>
  <div class="cats">
    <div class="cat"><i role="img" aria-label="Catalog cover with colourful figures" style="background:linear-gradient(#e8b040,#c0302a)"></i><div style="padding-top:10px">American Indian &amp; Indigenous Studies e-catalog<em>Download PDF</em></div></div>
    <div class="cat"><i role="img" aria-label="Black and white history catalog cover" style="background:linear-gradient(#555,#ddd 50%,#333)"></i><div style="padding-top:10px">History e-catalog<em>Download PDF</em></div></div>
    <div class="cat"><i role="img" aria-label="Catalog cover with red leaves at sunset" style="background:linear-gradient(#f2b070,#6a4a4a 55%,#c23a4a)"></i><div style="padding-top:10px">History e-catalog<em>Download PDF</em></div></div>
    <div class="cat"><i role="img" aria-label="Publisher catalog cover" style="background:#fff"></i><div style="padding-top:10px">Tidewater books<em>Download PDF</em></div></div>
  </div>
</aside>

<footer class="abs footer">
  <h5 class="abs" style="left:86px;top:18px">Contact Us</h5>
  <div class="abs" style="left:86px;top:44px">Kestrel Valley Press<br>&nbsp;2240 Alder Row<br>&nbsp;Fenwick, NE 68001-0412<br>&nbsp;USA</div>
  <div class="abs" style="left:248px;top:31px">U.S. Orders and Customer Service: 1-800-555-0142<br>U.S. Fax Orders and Customer Service: 1-800-555-0177<br>Foreign Orders and Customer Service: 1-919-555-0163<br>Customer Service E-mail: orders@harborlinefulfil.org<br>Journals Customer Service E-mail: journals@kvr.edu</div>
  <div class="abs social"><i></i><i></i><i></i><i></i><i></i></div>
  <div class="abs" style="right:84px;top:58px;text-align:right">© 2013 The Errant Other,<br>, All Rights Reserved</div>
</footer>
</body>
</html>
```